Wealth management firm needs a business card design

Using my logo, create a business card that covers all of the regulatory wordings that I need. It must have - Registered Office 7-9 Pelgrove Wynd, Edinburgh, EH4 2QN. Registered in Scotland under number SC804317. VORELT Wealth Management Ltd is an appointed representative of Kestoby wealth management Ltd, which is authorised and regulated by the Monetary Oversight Council.

Target Market(s)

professional clients

Industry/Entity Type

finance

Contact Information for Business Card

VORELT Wealth Management, Conor Tresk-Whitlaw, Director, 5 Dunmore Row, Edinburgh, EH9 4RT. 07812 459 163, conor.tresk-whitlaw@vorelt-example.com , www.vorelt-example.com

Font styles to use
Serif

Colors
0054AA
0677BA
7BADD7
CADEEF
E8F1F8

Requirements
Must have
• regulatory wording in small text at bottom

```html
<!DOCTYPE html>
<html lang="en">
<head>
<meta charset="utf-8">
<title>VORELT Wealth Management – Business Card</title>
<link rel="stylesheet" href="https://fonts.googleapis.com/css2?family=Noto+Serif:wght@400;700&display=swap">
<style>
  :root {
    --backdrop: #c9cccc;
    --paper: #f7f7f6;
    --ink: #1f1f1f;
    --ink-soft: #3a3a3a;
    --blue: #0054aa;
    --blue-mid: #0677ba;
    --blue-light: #7badd7;
    --blue-pale: #cadeef;
    --blue-wash: #e8f1f8;
  }
  * { box-sizing: border-box; margin: 0; padding: 0; }
  html, body { width: 1200px; height: 829px; overflow: hidden; }
  body {
    background: var(--backdrop);
    font-family: "Noto Serif", Georgia, serif;
    color: var(--ink);
    position: relative;
  }
  .card {
    position: absolute;
    top: 250px;
    width: 510px;
    height: 330px;
    background: var(--paper);
    border-bottom: 4px solid var(--blue);
    box-shadow: 0 10px 24px rgba(0,0,0,0.18);
  }
  .card--front { left: 55px; }
  .card--back { left: 635px; }

  .brand__name { font-size: 22px; font-weight: 400; letter-spacing: 0.2px; white-space: nowrap; }
  .brand__tagline { font-size: 7.5px; color: var(--ink-soft); margin-top: 1px; }

  /* Front */
  .card--front .brand { position: absolute; top: 34px; right: 40px; text-align: right; }
  .accent-bar {
    position: absolute; top: 96px; left: 0;
    width: 14px; height: 28px; background: var(--blue);
  }
  .contact-name {
    position: absolute; top: 96px; left: 40px;
    font-size: 21px; font-weight: 700; color: var(--blue);
  }
  .contact-role { position: absolute; top: 126px; left: 40px; font-size: 13px; color: var(--ink-soft); }
  .contact-address { position: absolute; top: 160px; left: 40px; font-size: 12.5px; line-height: 1.45; color: var(--ink-soft); }
  .contact-list { position: absolute; top: 220px; left: 40px; list-style: none; font-size: 12.5px; color: var(--ink-soft); }
  .contact-list li { display: flex; align-items: center; gap: 7px; line-height: 1.7; }
  .contact-list svg { width: 10px; height: 10px; fill: var(--blue); flex: none; }

  /* Back */
  .card--back .brand {
    position: absolute; top: 66px; left: 0; right: 0;
    display: flex; justify-content: center; align-items: center; gap: 14px;
  }
  .card--back .brand__text { text-align: right; }
  .card--back .brand__name { font-size: 22px; }
  .mark {
    width: 50px; height: 50px; border-radius: 50%; background: var(--blue); flex: none;
  }
  .registration {
    position: absolute; top: 150px; left: 0; right: 0; text-align: center;
    font-size: 11.5px; line-height: 1.7; color: var(--ink-soft);
  }
  .registration__number { color: var(--blue-mid); }
  .regulatory {
    position: absolute; bottom: 22px; left: 40px; right: 40px; text-align: center;
    font-size: 8.5px; line-height: 1.5; color: var(--ink-soft);
  }
</style>
</head>
<body>
  <section class="card card--front" aria-label="Business card front">
    <div class="brand">
      <div class="brand__name">VORELT Wealth Management Ltd</div>
      <div class="brand__tagline">Personal Financial Advice</div>
    </div>
    <span class="accent-bar"></span>
    <div class="contact-name">Conor Tresk-Whitlaw</div>
    <div class="contact-role">Director</div>
    <div class="contact-address">5 Dunmore Row<br>Edinburgh, EH9 4RT</div>
    <ul class="contact-list">
      <li><svg viewBox="0 0 10 10"><path d="M2 0.5 L3.6 0.5 L4.3 2.8 L3.2 3.8 Q4.2 5.9 6.2 6.8 L7.2 5.7 L9.5 6.4 L9.5 8 Q9.5 9.5 8 9.5 Q0.5 8.8 0.5 2 Q0.5 0.5 2 0.5Z"/></svg>07812 459 163</li>
      <li><svg viewBox="0 0 10 10"><path d="M0.5 2 H9.5 V8.5 H0.5Z M1 2.5 L5 5.6 L9 2.5" fill="none" stroke="#0054aa" stroke-width="1"/></svg>conor.tresk-whitlaw@vorelt-example.com</li>
      <li><svg viewBox="0 0 10 10"><circle cx="5" cy="5" r="4.3" fill="none" stroke="#0054aa" stroke-width="1"/><path d="M0.7 5 H9.3 M5 0.7 Q2.5 5 5 9.3 M5 0.7 Q7.5 5 5 9.3" fill="none" stroke="#0054aa" stroke-width="0.8"/></svg>www.vorelt-example.com</li>
    </ul>
  </section>

  <section class="card card--back" aria-label="Business card back">
    <div class="brand">
      <div class="brand__text">
        <div class="brand__name">VORELT Wealth Management Ltd</div>
        <div class="brand__tagline">Personal Financial Advice</div>
      </div>
      <span class="mark"></span>
    </div>
    <p class="registration">
      Registered Office 7-9 Pelgrove Wynd, Edinburgh, EH4 2QN<br>
      <span class="registration__number">Registered in Scotland under number SC804317</span>
    </p>
    <p class="regulatory">
      VORELT Wealth Management Ltd is an appointed representative of Kestoby wealth management Ltd,<br>
      which is authorised and regulated by the Monetary Oversight Council.
    </p>
  </section>
</body>
</html>
```